Logo redesign for car wrap

Hello, We are looking for someone to create 10-20 different versions of our logo that could potentially go on the side of a service van. We do not want a full wrap. We just want something for the back of the van and for the sides to be a mirrored image of the other side. Something simple would be best. Due date for this project is 04/25, hiring immediately.

We want the color of every asset to be in our blue CMYK:91,66,0,0
We want to change the Measure and Spread logo from "top it, Fill it, Slice it" to "Topping Equipment, Filling Equipment, and Slicing Equipment"

(Here are the van dimensions and see below for pictures of the new van as well as a picture of what we have done in the past. The dimensions of van panel are 28 ¾ tall and 53 ½ wide exact.)

```html
<!DOCTYPE html>
<html lang="en">
<head>
<meta charset="UTF-8">
<title>Measure and Spread – Van Rear Panel</title>
<link href="https://fonts.googleapis.com/css2?family=Russo+One&family=Josefin+Sans:wght@400&display=swap" rel="stylesheet">
<style>
  :root {
    --brand-blue: #2b6fd6;
    --ink: #4a4a4c;
    --panel: #ffffff;
  }
  html, body {
    margin: 0;
    padding: 0;
    width: 1200px;
    height: 900px;
    overflow: hidden;
    background: var(--panel);
  }
  .van-panel {
    position: relative;
    width: 1200px;
    height: 900px;
    background: var(--panel);
  }
  .company-name {
    position: absolute;
    left: 0;
    right: 0;
    top: 215px;
    margin: 0;
    text-align: center;
    font-family: "Russo One", sans-serif;
    font-weight: 400;
    font-size: 66px;
    letter-spacing: 0.01em;
    color: var(--ink);
  }
  .service-list {
    position: absolute;
    left: 0;
    right: 0;
    top: 380px;
    margin: 0;
    padding: 0;
    list-style: none;
    text-align: center;
    font-family: "Josefin Sans", sans-serif;
    font-weight: 400;
    font-size: 32px;
    letter-spacing: 0.2em;
    color: var(--ink);
  }
  .service-list li {
    height: 96px;
    line-height: 96px;
  }
  .machine-art {
    position: absolute;
    top: 370px;
    width: 210px;
    height: 230px;
    border-radius: 8px;
    background: linear-gradient(180deg, rgba(43,111,214,0.18), rgba(43,111,214,0.32));
  }
  .machine-art--left { left: 60px; }
  .machine-art--right { right: 60px; }
</style>
</head>
<body>
  <main class="van-panel">
    <h1 class="company-name">MEASURE AND SPREAD</h1>

    <div class="machine-art machine-art--left" role="img" aria-label="Blue line illustration of a food topping and filling machine with hopper and control panel"></div>

    <ul class="service-list">
      <li>TOPPING EQUIPMENT</li>
      <li>FILLING EQUIPMENT</li>
      <li>SLICING EQUIPMENT</li>
    </ul>

    <div class="machine-art machine-art--right" role="img" aria-label="Mirrored blue line illustration of a food topping and filling machine with hopper and control panel"></div>
  </main>
</body>
</html>
```